Quorvel Landing page redesign

We are looking for a landing page redesign before we officially launch. We want to incorporate the information already on the site at www.Quorvel-example.com landing page but make it more inviting. There needs to be a sign up section along with clearly stating what we do. Having a place for sample profiles and linking to our blog and podcast is option. More information about all we will be doing is at Quorvel is on the landing page and also on the blog.

Target Market(s)

35 years old and up.

Coding

Coded - Design and coding required

Number of Pages Required

1 page

Requirements
Must have
• The top bar and the bottom bar (with the privacy policy, etc)
• Sign in/up section.
• I don't want to give to much here because I want designers to be creative.
Nice to have
• Prefer not to have a landing page that requires a lot of scrolling at all.

```html
<!DOCTYPE html>
<html lang="en">
<head>
<meta charset="utf-8">
<title>Quorvel</title>
<link href="https://fonts.googleapis.com/css2?family=Roboto:ital,wght@0,300;0,400;0,500;1,400;1,500&display=swap" rel="stylesheet">
<style>
  :root {
    --hero-bg: #5d6a8c;
    --ring-outer: #8f97b1;
    --ring-mid: #bcc1d2;
    --disc: #dfe1ea;
    --ink: #1a2146;
    --text: #4a4d5c;
    --white: #ffffff;
    --accent: #5b6689;
    --icon: #d6d6d8;
    --night: #1a2449;
    --night-low: #2a3458;
    --footer: #111c42;
  }
  * { box-sizing: border-box; margin: 0; padding: 0; }
  html, body { width: 1200px; height: 1037px; overflow: hidden; }
  body { font-family: "Roboto", sans-serif; position: relative; background: var(--white); }

  .hero {
    position: absolute; left: 0; top: 0; width: 1200px; height: 632px;
    background: var(--hero-bg); overflow: hidden;
  }
  .hero-tree {
    position: absolute; left: 30px; top: 100px; width: 1140px; height: 532px;
    background: radial-gradient(ellipse at 50% 60%, rgba(140,150,182,.45), rgba(93,106,140,0) 70%);
  }
  .nav-links { position: absolute; left: 135px; top: 48px; display: flex; gap: 29px; }
  .nav-links a { color: var(--white); text-decoration: none; font-size: 15px; }
  .auth { position: absolute; left: 902px; top: 44px; display: flex; gap: 8px; }
  .auth a {
    display: block; height: 30px; line-height: 30px; padding: 0 15px;
    background: var(--white); border-radius: 15px; color: var(--accent);
    text-decoration: none; font-size: 15px;
  }
  .ring { position: absolute; border-radius: 50%; }
  .ring-outer { left: 328px; top: 45px; width: 544px; height: 544px; background: var(--ring-outer); box-shadow: 0 0 60px rgba(40,48,80,.45); }
  .ring-mid { left: 356px; top: 73px; width: 488px; height: 488px; background: var(--ring-mid); }
  .ring-inner { left: 387px; top: 104px; width: 426px; height: 426px; background: var(--disc); }

  .brand {
    position: absolute; left: 0; width: 1200px; top: 222px; text-align: center;
    font-size: 28px; line-height: 34px; font-weight: 400; color: var(--ink);
  }

  .hero-copy {
    position: absolute; left: 410px; top: 268px; width: 380px; text-align: center;
    font-size: 17px; line-height: 27px; color: var(--text); font-weight: 400;
  }
  .hero-copy em { font-weight: 500; }
  .samples { position: absolute; left: 429px; top: 360px; display: flex; gap: 6px; }
  .samples a {
    display: block; width: 168px; height: 38px; line-height: 38px; border-radius: 19px;
    font-size: 13px; font-weight: 500; text-decoration: none; text-align: center;
  }
  .btn-light { background: var(--white); color: var(--ink); }
  .btn-dark { background: var(--accent); color: var(--white); }

  .features { position: absolute; left: 0; top: 632px; width: 1200px; height: 176px; background: var(--white); }
  .feature { position: absolute; top: 44px; width: 180px; height: 90px; text-align: center; }
  .feature svg { position: absolute; left: 50%; top: 4px; transform: translateX(-50%); }
  .feature p { position: relative; top: 22px; font-size: 14px; line-height: 19px; font-weight: 300; color: var(--ink); }
  .feature b { font-weight: 500; }

  .signup {
    position: absolute; left: 0; top: 808px; width: 1200px; height: 182px;
    background: linear-gradient(180deg, var(--night) 0%, var(--night) 65%, var(--night-low) 100%);
  }
  .balloon { position: absolute; top: 24px; width: 72px; height: 90px; border-radius: 50% 50% 45% 45%;
    background: radial-gradient(circle at 40% 35%, #4a4f7a, #262b4f 75%); }
  .balloon-left { left: 139px; }
  .balloon-right { left: 990px; }
  .signup h2 { position: absolute; left: 0; width: 1200px; top: 40px; text-align: center; color: var(--white); font-size: 21px; font-weight: 500; }
  .signup-form { position: absolute; left: 292px; top: 74px; width: 616px; height: 51px; display: flex; border-radius: 26px; overflow: hidden; }
  .signup-form input { flex: 1; border: none; padding-left: 21px; font-family: inherit; font-size: 13px; color: var(--text); background: var(--white); outline: none; }
  .signup-form input::placeholder { color: #8a8d99; }
  .signup-form button { width: 165px; border: none; background: var(--accent); color: var(--white); font-family: inherit; font-size: 17px; }
  .signin-note { position: absolute; left: 0; width: 1200px; top: 144px; text-align: center; color: #c4c7d3; font-size: 13px; font-weight: 500; }
  .signin-note a { color: var(--white); font-size: 16px; font-weight: 400; margin-left: 9px; }

  .site-footer { position: absolute; left: 0; top: 990px; width: 1200px; height: 47px; background: var(--footer); color: var(--white); font-size: 13px; text-align: center; line-height: 47px; }
</style>
</head>
<body>
  <header class="hero">
    <div class="hero-tree" role="img" aria-label="Soft silhouette of a leafy family tree spreading across the background"></div>
    <nav class="nav-links"><a href="#">Blog</a><a href="#">Podcast</a></nav>
    <div class="auth"><a href="#">Sign up</a><a href="#">Log in</a></div>
    <div class="ring ring-outer"></div>
    <div class="ring ring-mid"></div>
    <div class="ring ring-inner"></div>
    <div class="brand">Quorvel</div>
    <p class="hero-copy"><em>Build</em> multiple Quorvel pages through one account for yourself, your family and to keep loved one's legacies alive.</p>
    <div class="samples">
      <a class="btn-light" href="#">Sample Quorvel Profile</a>
      <a class="btn-dark" href="#">Sample Legacy Profile</a>
    </div>
  </header>

  <section class="features">
    <div class="feature" style="left:136px">
      <svg width="80" height="80" viewBox="0 0 80 80" fill="none" stroke="var(--icon)" stroke-width="5"><path d="M18 70 L14 52 L52 14 L68 30 L30 68 Z"/><path d="M14 52 L30 68"/></svg>
      <p><b>Create</b> Timelines, Maps,<br>Family Trees</p>
    </div>
    <div class="feature" style="left:324px">
      <svg width="80" height="80" viewBox="0 0 80 80" fill="none" stroke="var(--icon)" stroke-width="5"><path d="M40 72 L12 42 C2 30 10 12 25 12 C33 12 38 18 40 22 C42 18 47 12 55 12 C70 12 78 30 68 42 Z"/></svg>
      <p><b>Memorialize</b> Loved<br>Ones</p>
    </div>
    <div class="feature" style="left:509px">
      <svg width="80" height="80" viewBox="0 0 80 80" fill="none" stroke="var(--icon)" stroke-width="5"><circle cx="40" cy="16" r="9"/><circle cx="16" cy="64" r="9"/><circle cx="64" cy="60" r="9"/><path d="M35 24 L21 56 M45 24 L59 52"/></svg>
      <p><b>Share</b> Family Stories,<br>History and more Maps,</p>
    </div>
    <div class="feature" style="left:698px">
      <svg width="90" height="80" viewBox="0 0 90 80" fill="none" stroke="var(--icon)" stroke-width="5"><ellipse cx="45" cy="40" rx="40" ry="30"/><circle cx="45" cy="40" r="14"/></svg>
      <p><b>Control</b> Your<br>Privacy</p>
    </div>
    <div class="feature" style="left:884px">
      <svg width="90" height="90" viewBox="0 0 90 90" fill="none" stroke="var(--icon)" stroke-width="5"><path d="M22 78 L62 40 L52 30 L12 68 Z"/><path d="M68 6 V30 M56 18 H80"/></svg>
      <p><b>No</b> Ads, No Like Buttons<br><b>No</b> News Feeds</p>
    </div>
  </section>

  <section class="signup">
    <div class="balloon balloon-left" role="img" aria-label="Hot air balloon drifting in the night sky"></div>
    <div class="balloon balloon-right" role="img" aria-label="Hot air balloon drifting in the night sky"></div>
    <h2>Become an Early User</h2>
    <form class="signup-form">
      <input type="email" placeholder="Type Your Email Adress">
      <button type="button">Subscribe</button>
    </form>
    <p class="signin-note">Already Have an Account? <a href="#">Sign in</a></p>
  </section>

  <footer class="site-footer">Copyright © 2017 Quorvel All Rights Reserved.</footer>
</body>
</html>
```